Business to Business Website Homepage Design

Hi, My Web Developer is giving me designs that aren't quite taking my fancy as far as visual impact. I'd love to see designs come out which are simple, fresh and powerful.
I just want a PDF document that I can give to my web developer to follow, so this project is NOT to make a website, its to design the homepage.
I would like it to scroll down through different areas of my website on the homepage. Our colours are Blood Orange, White, Grey & Black.
I like these websites:
Simplicity
https://www.quenzaro.com/au/webapps/mpp/home
Our Team Section
http://bremlitch.com.au/
We'd like our logo on top left. Nav bar top right. Have an image which we can place a headline subject on + video icon which will pop out with a video and opt in for name and email with a heading so people know what they're opting in for.
The next section should have a lot of white space, this "What we do" which is 1) Grow in size so your business can get bigger 2) increase in value, so you maximise what your business is worth 3) Free up your time, so you can live the lifestyle you've always wanted. Our brief was we want image/text combo with a lot of white space,
Then we have our services
After Services, would like to have a "Why Work With Us" section
Then a testimonials section
Then "Our Team"
Then contact us.
Thats pretty much it, we'd just love some different ideas, these guys are almost there, but just need more impact.
Updates
Target Market(s)
Business Owners between $1m to $3m turnover
Industry/Entity Type
Business
Number of Pages Required
1 page
Look and feel
Each slider illustrates characteristics of the customer's brand and the style your logo design should communicate.

```html
<!DOCTYPE html>
<html lang="en">
<head>
<meta charset="utf-8">
<title>Lodestar Alliance — Home</title>
<link rel="stylesheet" href="https://fonts.googleapis.com/css2?family=Open+Sans:wght@300;400;600;700&display=swap">
<style>
:root{
  --red:#e5332a;
  --red-dark:#c92a22;
  --ink:#1c1c1c;
  --text:#444;
  --muted:#666;
  --white:#fff;
  --grey:#e6e6e6;
  --navy:#141a24;
  --black:#0b0d12;
}
*{box-sizing:border-box;margin:0;padding:0}
html,body{width:1200px;height:4675px;overflow:hidden}
body{font-family:"Open Sans",Arial,sans-serif;color:var(--text);background:var(--white);position:relative}
.abs{position:absolute}
.btn{position:absolute;background:var(--red);color:var(--white);font-size:11px;font-weight:600;text-transform:uppercase;display:flex;align-items:center;justify-content:center;letter-spacing:.3px}
.center{text-align:center}
h2.section-title{position:absolute;left:0;width:1200px;text-align:center;font-size:24px;font-weight:700;color:var(--ink);letter-spacing:.5px;line-height:32px}
.lead{position:absolute;left:190px;width:820px;text-align:center;font-size:12.5px;line-height:25px;color:var(--muted)}

/* Header / hero */
.hero{position:absolute;left:0;top:0;width:1200px;height:583px;background:linear-gradient(160deg,#3a4150 0%,#222834 45%,#12161e 100%)}
.brand{position:absolute;left:64px;top:50px;display:flex;align-items:center;gap:10px}
.brand-mark{width:30px;height:30px;border-radius:50%;background:var(--red)}
.brand-name{font-size:22px;font-weight:700;color:var(--red);letter-spacing:1px}
.nav{position:absolute;top:58px;left:452px;display:flex;gap:44px;font-size:11px;font-weight:600;color:var(--white)}
.burger{position:absolute;left:1126px;top:56px;width:18px}
.burger span{display:block;height:3px;background:var(--white);margin-bottom:3px}
.hero-title{position:absolute;top:202px;left:0;width:1200px;text-align:center;font-size:33px;font-weight:400;color:var(--white)}
.hero-title i{font-style:normal;color:var(--red);margin:0 8px}
.hero-sub{position:absolute;top:262px;left:0;width:1200px;text-align:center;font-size:18px;color:#e8e8e8}
.play{position:absolute;left:556px;top:400px}

/* Feature rows */
.row-img{position:absolute;width:600px;height:400px}
.row-text{position:absolute;width:440px}
.row-text h3{font-size:33px;font-weight:300;color:var(--ink);line-height:38px}
.row-text h4{font-size:23px;font-weight:700;color:var(--ink);line-height:29px;text-transform:uppercase}
.row-text p{font-size:11.5px;line-height:24px;color:var(--muted);margin-top:14px}

/* Services */
.service{position:absolute;width:320px}
.service svg{position:absolute;left:0;top:0}
.service h5{position:absolute;left:56px;top:4px;font-size:13px;font-weight:700;color:var(--ink);text-transform:uppercase}
.service p{position:absolute;left:56px;top:28px;width:260px;font-size:11.5px;line-height:24px;color:var(--muted)}
.service .btn{left:56px;top:118px;width:90px;height:30px;font-size:10px;text-transform:none}

/* Why */
.why{position:absolute;left:0;top:2659px;width:1200px;height:371px;background:var(--grey)}

/* Testimonials */
.testimonials{position:absolute;left:0;top:3030px;width:1200px;height:423px;background:linear-gradient(180deg,#1c2230,#2a3140 55%,#171b24)}

/* Team */
.team-grid{position:absolute;left:0;top:3688px;width:1200px;height:458px;display:grid;grid-template-columns:repeat(5,240px);grid-template-rows:repeat(2,229px)}
.team-tile{background:linear-gradient(160deg,#c9a78e,#7d5d4b)}
.team-tile.alt{background:linear-gradient(160deg,#b7b0a8,#6e6258)}
.team-tile.featured{background:var(--red);color:var(--white);display:flex;flex-direction:column;align-items:center;justify-content:center;opacity:.92}
.team-tile.featured b{font-size:16px;font-weight:700}
.team-tile.featured span{font-size:11px;margin-top:4px}

/* Contact */
.contact{position:absolute;left:0;top:4146px;width:1200px;height:436px;background:linear-gradient(180deg,#1b2130,#0f131b)}
.field{position:absolute;border:1px solid #cfd3da;color:var(--white);font-size:11px;padding:8px 10px}

/* Footer */
.footer{position:absolute;left:0;top:4582px;width:1200px;height:93px;background:var(--black);color:#ddd;font-size:11px}
.social{width:24px;height:24px;border-radius:50%;background:#bbb;display:inline-block;margin-left:6px;vertical-align:middle}
</style>
</head>
<body>

<header class="hero" role="img" aria-label="Dark photo of a business person working on a laptop">
  <div class="brand"><span class="brand-mark"></span><span class="brand-name">LODESTAR</span></div>
  <nav class="nav"><span>WHAT WE DO</span><span>SERVICES</span><span>WHY WORK WITH US</span><span>TESTIMONIALS</span><span>OUR TEAM</span><span>CONTACT US</span></nav>
  <div class="burger"><span></span><span></span><span></span></div>
  <h1 class="hero-title">Your Business<i>•</i>Your Success<i>•</i>Your life Style</h1>
  <p class="hero-sub">We exist to help people create better livelihoods so they can follow their dreams and live life to its fullest</p>
  <div class="btn" style="left:518px;top:313px;width:164px;height:50px;font-size:13px">Sign up now</div>
  <svg class="play" width="74" height="74" viewBox="0 0 74 74" aria-hidden="true">
    <circle cx="37" cy="37" r="34" fill="none" stroke="rgba(255,255,255,.25)" stroke-width="3"/>
    <path d="M29 24 L52 37 L29 50Z" fill="rgba(255,255,255,.25)"/>
  </svg>
</header>

<section class="what-we-do">
  <h2 class="section-title" style="top:640px">WHAT WE DO</h2>
  <p class="lead" style="top:695px">It is a long established fact that a reader will be distracted by the readable content of a page when looking at its layout. The point of using Lorem Ipsum is that it has a more-or-less normal distribution of letters, as opposed to using...</p>

  <div class="row-img" style="left:0;top:806px;background:linear-gradient(135deg,#7fb0d0,#2f5f86 60%,#1d2f45)" role="img" aria-label="Hands typing on a laptop keyboard"></div>
  <div class="row-text" style="left:686px;top:860px">
    <h3>GROW IN SIZE SO</h3>
    <h4>So your business can get bigger</h4>
    <p>It is a long established fact that a reader will be distracted by the readable content of a page when looking at its layout. The point of using Lorem Ipsum is that it has a more-or-less normal distribution of letters, as opposed to using 'Content here, content here', making it look like readable English.</p>
  </div>
  <div class="btn" style="left:686px;top:1067px;width:200px;height:44px">Click here for more info</div>

  <div class="row-text" style="left:75px;top:1262px">
    <h3>INCREASE IN VALUE</h3>
    <h4>So you maximise what your<br>business is worth</h4>
    <p>It is a long established fact that a reader will be distracted by the readable content of a page when looking at its layout. The point of using Lorem Ipsum is that it has a more-or-less normal distribution of letters, as opposed to using 'Content here, content here', making it look like readable English.</p>
  </div>
  <div class="btn" style="left:75px;top:1494px;width:200px;height:44px">Click here for more info</div>
  <div class="row-img" style="left:600px;top:1206px;background:linear-gradient(135deg,#d7dde3,#8795a4 55%,#2e3a4a)" role="img" aria-label="Smiling businessman in a suit at a desk"></div>

  <div class="row-img" style="left:0;top:1605px;background:linear-gradient(135deg,#f0f0f0,#9a9a9a 50%,#2a2a2a)" role="img" aria-label="Black and white close-up of a man adjusting his wristwatch"></div>
  <div class="row-text" style="left:686px;top:1670px">
    <h3>FREE UP YOUR TIME</h3>
    <h4>So you can live the lifestyle<br>you've always wanted.</h4>
    <p>It is a long established fact that a reader will be distracted by the readable content of a page when looking at its layout. The point of using Lorem Ipsum is that it has a more-or-less normal distribution of letters, as opposed to using 'Content here, content here', making it look like readable English.</p>
  </div>
  <div class="btn" style="left:686px;top:1900px;width:200px;height:44px">Click here for more info</div>
</section>

<section class="services">
  <h2 class="section-title" style="top:2084px">OUR SERVICES</h2>
  <p class="lead" style="top:2128px">Lorem Ipsum is simply dummy text of the printing and typesetting industry. Lorem Ipsum has been the industry's standard dummy text ever since the 1500s, when an unknown printer took a galley of type and scrambled it to make a type specimen book.</p>

  <div class="service" style="left:97px;top:2237px">
    <svg width="40" height="30" viewBox="0 0 40 30"><circle cx="20" cy="8" r="6" fill="var(--red)"/><path d="M9 28c0-7 5-11 11-11s11 4 11 11z" fill="var(--red)"/><circle cx="7" cy="11" r="4" fill="var(--red)"/><circle cx="33" cy="11" r="4" fill="var(--red)"/></svg>
    <h5>People</h5><p>It is a long established fact that a reader will be distracted by the readable content of a page when looking...</p><div class="btn">Read More</div>
  </div>
  <div class="service" style="left:458px;top:2237px">
    <svg width="40" height="30" viewBox="0 0 40 30"><path d="M18 4a13 13 0 1 0 13 13H18z" fill="var(--red)"/><path d="M21 1v13h13A13 13 0 0 0 21 1z" fill="var(--red)"/></svg>
    <h5>Business Systems</h5><p>It is a long established fact that a reader will be distracted by the readable content of a page when looking...</p><div class="btn">Read More</div>
  </div>
  <div class="service" style="left:804px;top:2237px">
    <svg width="40" height="34" viewBox="0 0 40 34"><text x="4" y="30" font-family="Open Sans,Arial,sans-serif" font-size="34" font-weight="700" fill="var(--red)">$</text></svg>
    <h5>Funding</h5><p>It is a long established fact that a reader will be distracted by the readable content of a page when looking...</p><div class="btn">Read More</div>
  </div>
  <div class="service" style="left:97px;top:2437px">
    <svg width="40" height="30" viewBox="0 0 40 30"><path d="M4 12h32v16H4z M2 6h36v6H2z" fill="var(--red)"/><path d="M20 6v22" stroke="#fff" stroke-width="3"/></svg>
    <h5>New Earning Streams</h5><p>It is a long established fact that a reader will be distracted by the readable content of a page when looking...</p><div class="btn">Read More</div>
  </div>
  <div class="service" style="left:458px;top:2437px">
    <svg width="40" height="30" viewBox="0 0 40 30"><rect x="8" y="1" width="22" height="28" rx="2" fill="var(--red)"/><rect x="12" y="7" width="14" height="3" fill="#fff"/><rect x="12" y="13" width="14" height="3" fill="#fff"/><rect x="12" y="19" width="9" height="3" fill="#fff"/></svg>
    <h5>New Markets</h5><p>It is a long established fact that a reader will be distracted by the readable content of a page when looking...</p><div class="btn">Read More</div>
  </div>
  <div class="service" style="left:804px;top:2437px">
    <svg width="40" height="30" viewBox="0 0 40 30"><rect x="3" y="18" width="6" height="10" fill="var(--red)"/><rect x="12" y="12" width="6" height="16" fill="var(--red)"/><rect x="21" y="6" width="6" height="22" fill="var(--red)"/><rect x="30" y="1" width="6" height="27" fill="var(--red)"/></svg>
    <h5>New Business</h5><p>It is a long established fact that a reader will be distracted by the readable content of a page when looking...</p><div class="btn">Read More</div>
  </div>
</section>

<section class="why">
  <h2 class="section-title" style="top:62px">WHY WORK WITH US</h2>
  <p class="abs center" style="top:108px;left:0;width:1200px;font-size:14px;color:#555">LOREM IPSUM IS SIMPLY DUMMY TEXT OF THE PRINTING AND TYPESETTING INDUSTRY.</p>
  <p class="lead" style="top:150px;left:170px;width:860px">Lorem Ipsum is simply dummy text of the printing and typesetting industry. Lorem Ipsum has been the industry's standard dummy text ever since the 1500s, when an unknown printer took a galley of type and scrambled it to make a type specimen book. It has survived not only five centuries, but also the leap into electronic typesetting, remaining essentially unchanged. It was popularised in the 1960s...</p>
  <div class="btn" style="left:498px;top:255px;width:204px;height:46px">Click here for more info</div>
</section>

<section class="testimonials" role="img" aria-label="Dark blurred photo of people in a business meeting">
  <h2 class="section-title" style="top:78px;color:var(--white)">TESTIMONIALS</h2>
  <span class="abs" style="left:150px;top:196px;color:rgba(255,255,255,.4);font-size:26px">‹</span>
  <span class="abs" style="left:1040px;top:196px;color:rgba(255,255,255,.4);font-size:26px">›</span>
  <span class="abs" style="left:236px;top:138px;color:#fff;font-size:30px;line-height:30px">“</span>
  <span class="abs" style="left:946px;top:200px;color:#fff;font-size:30px;line-height:30px">”</span>
  <p class="abs center" style="left:275px;top:148px;width:660px;font-size:13px;line-height:25px;color:#eee">Es simplemente el texto de relleno de las imprentas y archivos de texto. Lorem Ipsum ha sido el texto de relleno estándar de las industrias desde el año 1500, cuando un impresor (N. del T. persona que se dedica a la imprenta) desconocido usó una galería de textos y los mezcló de tal manera</p>
  <div class="abs" style="left:468px;top:256px;width:85px;height:85px;border-radius:50%;background:linear-gradient(135deg,#9aa3ad,#4d5560);border:3px solid #fff" role="img" aria-label="Portrait of the client giving the testimonial"></div>
  <p class="abs" style="left:572px;top:278px;color:#fff;font-size:13px">Marcus Hale</p>
  <p class="abs" style="left:572px;top:302px;color:#ccc;font-size:12px">Marketing executive</p>
</section>

<section class="team">
  <h2 class="section-title" style="top:3522px">OUR TEAM</h2>
  <p class="lead" style="top:3578px">It is a long established fact that a reader will be distracted by the readable content of a page when looking at its layout. The point of using Lorem Ipsum is that it has a more-or-less normal distribution of letters, as opposed to using...</p>
  <div class="team-grid">
    <div class="team-tile" role="img" aria-label="Team member portrait"></div>
    <div class="team-tile alt" role="img" aria-label="Team member portrait"></div>
    <div class="team-tile featured"><b>MARCUS HALE</b><span>TEAM CO-ORDINATOR</span></div>
    <div class="team-tile alt" role="img" aria-label="Team member portrait"></div>
    <div class="team-tile" role="img" aria-label="Team member portrait"></div>
    <div class="team-tile alt" role="img" aria-label="Team member portrait"></div>
    <div class="team-tile" role="img" aria-label="Team member portrait"></div>
    <div class="team-tile alt" role="img" aria-label="Team member portrait"></div>
    <div class="team-tile" role="img" aria-label="Team member portrait"></div>
    <div class="team-tile alt" role="img" aria-label="Team member portrait"></div>
  </div>
</section>

<section class="contact" role="img" aria-label="Dark photo of a city bridge at night">
  <h2 class="section-title" style="top:66px;color:var(--white)">CONTACT US</h2>
  <p class="abs center" style="top:120px;left:0;width:1200px;color:#ddd;font-size:13px">82 Alder Street, Adelaide, SA, 5000, Australia</p>
  <p class="abs center" style="top:156px;left:0;width:1200px;color:#ddd;font-size:13px">
    <svg width="12" height="12" viewBox="0 0 12 12" style="vertical-align:-1px"><path d="M2 1l3 0 1 3-2 1a7 7 0 0 0 3 3l1-2 3 1 0 3c-6 0-9-3-9-9z" fill="#ddd"/></svg> 08 7000 4512</p>
  <div class="field" style="left:315px;top:218px;width:277px;height:38px">Name :</div>
  <div class="field" style="left:315px;top:264px;width:277px;height:38px">Email :</div>
  <div class="field" style="left:315px;top:310px;width:277px;height:38px">Phone :</div>
  <div class="field" style="left:608px;top:218px;width:274px;height:84px">Message :</div>
  <div class="btn" style="left:608px;top:310px;width:274px;height:38px;font-size:12px">Submit</div>
</section>

<footer class="footer">
  <div class="abs" style="left:96px;top:32px;display:flex;align-items:center;gap:8px"><span class="brand-mark" style="width:24px;height:24px"></span><span style="font-size:17px;font-weight:700;color:var(--red)">LODESTAR</span></div>
  <p class="abs" style="left:346px;top:40px">Lodestar Alliance © 2015. Privacy Policy</p>
  <p class="abs" style="left:818px;top:40px">Connect with our social networks :</p>
  <div class="abs" style="left:990px;top:34px"><span class="social"></span><span class="social"></span><span class="social"></span><span class="social"></span></div>
</footer>

</body>
</html>
```